Webdesign für Projektmanagement
Zielgruppe
Projektmanagement und Projektsteuerung von Bauvorhaben für Projektentwickler und Bauträger.
Wesentliche Bereiche sind Wirtschaftliche Steuerung, Steuerung der Baustelle und Bauabläufe sowie Steuerung der Marketing und Vertriebsaktivitäten.
Aufgabenstellung
Orientierung am Logo. Logo und Visitenkarte liegen bei. Schriftart Prelo und Prelo Slab.

```html
<!DOCTYPE html>
<html lang="de">
<head>
<meta charset="utf-8">
<title>Kessling – Hero-Varianten</title>
<link rel="stylesheet" href="https://fonts.googleapis.com/css2?family=Raleway:ital,wght@0,200;0,300;0,400;0,500;0,700;1,400&display=swap">
<style>
  :root{
    --navy:#0b2844;
    --gold:#a8913f;
    --white:#ffffff;
    --card:#f2f2f2;
    --text:#3b3b3b;
    --line:#ececec;
  }
  *{box-sizing:border-box;margin:0;padding:0}
  html,body{width:701px;height:1200px;overflow:hidden;background:var(--navy)}
  body{position:relative;font-family:"Raleway",sans-serif}
  .variant{position:absolute;left:20px;width:663px;height:381px;overflow:hidden}
  .variant--dark{top:12px}
  .variant--warm{top:409px}
  .variant--gold{top:806px}

  .sidebar{position:absolute;left:0;top:0;width:101px;height:100%;background:var(--white)}
  .brand{position:absolute;left:15px;top:34px;font-weight:700;font-size:16px;color:var(--navy);letter-spacing:-0.2px}
  .nav{position:absolute;left:0;top:93px;width:101px;list-style:none;border-top:1px solid var(--line)}
  .nav li{height:20.2px;border-bottom:1px solid var(--line);display:flex;align-items:center;justify-content:space-between;padding:0 11px 0 16px;font-size:5.8px;font-weight:500;color:#222;letter-spacing:0.2px}
  .nav li.is-active{color:var(--gold);font-weight:700}
  .nav .chev{width:4px;height:4px;border-right:0.7px solid #999;border-top:0.7px solid #999;transform:rotate(45deg)}
  .nav .search{justify-content:flex-start;gap:5px;font-style:italic;font-weight:400;color:#888;text-transform:none}
  .social{position:absolute;left:23px;top:361px;display:flex;gap:6px}
  .social span{width:7px;height:7px;border-radius:50%;background:var(--navy)}

  .hero{position:absolute;left:101px;top:0;width:562px;height:100%}
  .variant--dark .hero{background:linear-gradient(120deg,#6a6460 0%,#857a6e 45%,#9a8d7c 75%,#7c7266 100%)}
  .variant--warm .hero{background:linear-gradient(110deg,#a08a64 0%,#c4a272 35%,#8f7a5c 60%,#b69a70 100%)}
  .variant--gold .hero{background:linear-gradient(115deg,#b8a862 0%,#c6b676 45%,#ad9c55 75%,#bcac68 100%)}

  .topbar{position:absolute;left:0;top:0;width:100%;height:19px;background:rgba(40,40,40,0.18);display:flex;align-items:center;padding-left:35px;gap:11px;font-size:5.6px;color:var(--white)}
  .topbar .item{display:flex;align-items:center;gap:3px}
  .topbar svg{width:6px;height:6px}

  .kicker{position:absolute;left:35px;top:96px;font-size:10.2px;letter-spacing:0.2px}
  .variant--dark .kicker{color:#c7a85a;font-weight:400}
  .variant--warm .kicker,.variant--gold .kicker{color:var(--navy);font-weight:700}
  .headline{position:absolute;left:34px;top:111px;font-weight:200;font-size:37px;line-height:37.5px;color:var(--white);letter-spacing:0.6px}

  .cards{position:absolute;left:35px;top:214px;display:flex;gap:6px}
  .card{position:relative;width:132px;height:93px;background:var(--card);padding:7px 8px 0}
  .card .cat{font-size:5.3px;font-style:italic;color:#666}
  .card .title{margin-top:5px;font-size:6.3px;font-weight:500;line-height:8.4px;color:var(--gold)}
  .card .body{margin-top:4px;font-size:5.4px;line-height:8.6px;color:var(--text)}
  .card .more{position:absolute;right:0;bottom:0;width:51px;height:13px;background:var(--navy);color:var(--white);font-size:4.9px;font-weight:700;display:flex;align-items:center;justify-content:center;letter-spacing:0.2px}

  .footer{position:absolute;left:0;bottom:0;width:100%;height:23px;background:rgba(255,255,255,0.18);display:flex;align-items:center;padding-left:35px;font-size:5.6px;color:#3a3a3a}
  .variant--dark .footer{color:#eee}
</style>
</head>
<body>

<section class="variant variant--dark">
  <aside class="sidebar">
    <div class="brand">Kessling</div>
    <ul class="nav">
      <li class="is-active">HOME</li><li>LEISTUNGEN</li><li>ÜBER UNS<i class="chev"></i></li><li>PROJEKTE<i class="chev"></i></li><li>PARTNER</li><li>KONTAKT</li><li class="search"><svg width="5" height="5" viewBox="0 0 10 10"><circle cx="4" cy="4" r="3" fill="none" stroke="#a8913f" stroke-width="1.6"/><line x1="6" y1="6" x2="9" y2="9" stroke="#a8913f" stroke-width="1.6"/></svg>Suchen</li>
    </ul>
    <div class="social"><span></span><span></span><span></span><span></span></div>
  </aside>
  <div class="hero" role="img" aria-label="Foto: Baupläne und Schutzhelm auf einem Arbeitstisch">
    <div class="topbar">
      <span class="item"><svg viewBox="0 0 10 10"><path d="M2 1l2 2-1 1.5c.6 1.3 1.3 2 2.5 2.5L7 6l2 2-1.5 1.5C4.5 9 1 5.5.5 2.5z" fill="#c7a85a"/></svg>+49 (0)211 - 555 012 34</span>
      <span class="item"><svg viewBox="0 0 10 10"><circle cx="5" cy="5" r="4" fill="none" stroke="#c7a85a"/><path d="M5 2.5V5h2" fill="none" stroke="#c7a85a"/></svg>Mo - Fr 9:00 - 18:00</span>
      <span class="item"><svg viewBox="0 0 10 10"><rect x="1" y="2.5" width="8" height="5.5" fill="none" stroke="#c7a85a"/><path d="M1 2.5l4 3 4-3" fill="none" stroke="#c7a85a"/></svg>info@kessling-re.de</span>
      <span class="item"><svg viewBox="0 0 10 10"><path d="M5 9.5C2.5 6 2 5 2 4a3 3 0 016 0c0 1-.5 2-3 5.5z" fill="#c7a85a"/><circle cx="5" cy="4" r="1" fill="#fff"/></svg>Lindenallee 12, 40210 Düsseldorf</span>
    </div>
    <p class="kicker">PROJEKTMANAGEMENT &amp; PROJEKTSTEUERUNG</p>
    <h1 class="headline">WIR REALISIEREN<br>BAUVORHABEN</h1>
    <div class="cards">
      <article class="card"><p class="cat">Betriebswirtschaftliche Planung</p><h2 class="title">STET CLITA KASD GUBERGREN NO SEA TAKIMATA SANCTUS EST LOREM</h2><p class="body">Lorem ipsum dolor sit amet, consetetur sadipscing elitr, sed diam nonumy eirmod tempor invidunt ut labore et dolore magna aliquyam erat, sed diam voluptua.</p><span class="more">WEITERLESEN</span></article>
      <article class="card"><p class="cat">Steuerung der baulichen Umsetzung</p><h2 class="title">STET CLITA KASD GUBERGREN NO SEA TAKIMATA SANCTUS EST LOREM</h2><p class="body">Lorem ipsum dolor sit amet, consetetur sadipscing elitr, sed diam nonumy eirmod tempor invidunt ut labore et dolore magna aliquyam erat, sed diam voluptua.</p><span class="more">WEITERLESEN</span></article>
      <article class="card"><p class="cat">Marketing und Vertrieb</p><h2 class="title">STET CLITA KASD GUBERGREN NO SEA TAKIMATA SANCTUS EST LOREM</h2><p class="body">Lorem ipsum dolor sit amet, consetetur sadipscing elitr, sed diam nonumy eirmod tempor invidunt ut labore et dolore magna aliquyam erat, sed diam voluptua.</p><span class="more">WEITERLESEN</span></article>
    </div>
    <div class="footer">© 2017 Kessling Real Estate GmbH - Impressum</div>
  </div>
</section>

<section class="variant variant--warm">
  <aside class="sidebar">
    <div class="brand">Kessling</div>
    <ul class="nav">
      <li class="is-active">HOME</li><li>LEISTUNGEN</li><li>ÜBER UNS<i class="chev"></i></li><li>PROJEKTE<i class="chev"></i></li><li>PARTNER</li><li>KONTAKT</li><li class="search"><svg width="5" height="5" viewBox="0 0 10 10"><circle cx="4" cy="4" r="3" fill="none" stroke="#a8913f" stroke-width="1.6"/><line x1="6" y1="6" x2="9" y2="9" stroke="#a8913f" stroke-width="1.6"/></svg>Suchen</li>
    </ul>
    <div class="social"><span></span><span></span><span></span><span></span></div>
  </aside>
  <div class="hero" role="img" aria-label="Foto: Bauleiter mit Tablet in warm beleuchteter Halle">
    <div class="topbar">
      <span class="item"><svg viewBox="0 0 10 10"><path d="M2 1l2 2-1 1.5c.6 1.3 1.3 2 2.5 2.5L7 6l2 2-1.5 1.5C4.5 9 1 5.5.5 2.5z" fill="#c7a85a"/></svg>+49 (0)211 - 555 012 34</span>
      <span class="item"><svg viewBox="0 0 10 10"><circle cx="5" cy="5" r="4" fill="none" stroke="#c7a85a"/><path d="M5 2.5V5h2" fill="none" stroke="#c7a85a"/></svg>Mo - Fr 9:00 - 18:00</span>
      <span class="item"><svg viewBox="0 0 10 10"><rect x="1" y="2.5" width="8" height="5.5" fill="none" stroke="#c7a85a"/><path d="M1 2.5l4 3 4-3" fill="none" stroke="#c7a85a"/></svg>info@kessling-re.de</span>
      <span class="item"><svg viewBox="0 0 10 10"><path d="M5 9.5C2.5 6 2 5 2 4a3 3 0 016 0c0 1-.5 2-3 5.5z" fill="#c7a85a"/><circle cx="5" cy="4" r="1" fill="#fff"/></svg>Lindenallee 12, 40210 Düsseldorf</span>
    </div>
    <p class="kicker">PROJEKTMANAGEMENT &amp; PROJEKTSTEUERUNG</p>
    <h1 class="headline">WIR REALISIEREN<br>BAUVORHABEN</h1>
    <div class="cards">
      <article class="card"><p class="cat">Betriebswirtschaftliche Planung</p><h2 class="title">STET CLITA KASD GUBERGREN NO SEA TAKIMATA SANCTUS EST LOREM</h2><p class="body">Lorem ipsum dolor sit amet, consetetur sadipscing elitr, sed diam nonumy eirmod tempor invidunt ut labore et dolore magna aliquyam erat, sed diam voluptua.</p><span class="more">WEITERLESEN</span></article>
      <article class="card"><p class="cat">Steuerung der baulichen Umsetzung</p><h2 class="title">STET CLITA KASD GUBERGREN NO SEA TAKIMATA SANCTUS EST LOREM</h2><p class="body">Lorem ipsum dolor sit amet, consetetur sadipscing elitr, sed diam nonumy eirmod tempor invidunt ut labore et dolore magna aliquyam erat, sed diam voluptua.</p><span class="more">WEITERLESEN</span></article>
      <article class="card"><p class="cat">Marketing und Vertrieb</p><h2 class="title">STET CLITA KASD GUBERGREN NO SEA TAKIMATA SANCTUS EST LOREM</h2><p class="body">Lorem ipsum dolor sit amet, consetetur sadipscing elitr, sed diam nonumy eirmod tempor invidunt ut labore et dolore magna aliquyam erat, sed diam voluptua.</p><span class="more">WEITERLESEN</span></article>
    </div>
    <div class="footer">© 2017 Kessling Real Estate GmbH - Impressum</div>
  </div>
</section>

<section class="variant variant--gold">
  <aside class="sidebar">
    <div class="brand">Kessling</div>
    <ul class="nav">
      <li class="is-active">HOME</li><li>LEISTUNGEN</li><li>ÜBER UNS<i class="chev"></i></li><li>PROJEKTE<i class="chev"></i></li><li>PARTNER</li><li>KONTAKT</li><li class="search"><svg width="5" height="5" viewBox="0 0 10 10"><circle cx="4" cy="4" r="3" fill="none" stroke="#a8913f" stroke-width="1.6"/><line x1="6" y1="6" x2="9" y2="9" stroke="#a8913f" stroke-width="1.6"/></svg>Suchen</li>
    </ul>
    <div class="social"><span></span><span></span><span></span><span></span></div>
  </aside>
  <div class="hero" role="img" aria-label="Foto: Architekt zeichnet an einem Plan, goldfarben eingefärbt">
    <div class="topbar">
      <span class="item"><svg viewBox="0 0 10 10"><path d="M2 1l2 2-1 1.5c.6 1.3 1.3 2 2.5 2.5L7 6l2 2-1.5 1.5C4.5 9 1 5.5.5 2.5z" fill="#0b2844"/></svg>+49 (0)211 - 555 012 34</span>
      <span class="item"><svg viewBox="0 0 10 10"><circle cx="5" cy="5" r="4" fill="none" stroke="#0b2844"/><path d="M5 2.5V5h2" fill="none" stroke="#0b2844"/></svg>Mo - Fr 9:00 - 18:00</span>
      <span class="item"><svg viewBox="0 0 10 10"><rect x="1" y="2.5" width="8" height="5.5" fill="none" stroke="#0b2844"/><path d="M1 2.5l4 3 4-3" fill="none" stroke="#0b2844"/></svg>info@kessling-re.de</span>
      <span class="item"><svg viewBox="0 0 10 10"><path d="M5 9.5C2.5 6 2 5 2 4a3 3 0 016 0c0 1-.5 2-3 5.5z" fill="#0b2844"/><circle cx="5" cy="4" r="1" fill="#fff"/></svg>Lindenallee 12, 40210 Düsseldorf</span>
    </div>
    <p class="kicker">PROJEKTMANAGEMENT &amp; PROJEKTSTEUERUNG</p>
    <h1 class="headline">WIR REALISIEREN<br>BAUVORHABEN</h1>
    <div class="cards">
      <article class="card"><p class="cat">Betriebswirtschaftliche Planung</p><h2 class="title">STET CLITA KASD GUBERGREN NO SEA TAKIMATA SANCTUS EST LOREM</h2><p class="body">Lorem ipsum dolor sit amet, consetetur sadipscing elitr, sed diam nonumy eirmod tempor invidunt ut labore et dolore magna aliquyam erat, sed diam voluptua.</p><span class="more">WEITERLESEN</span></article>
      <article class="card"><p class="cat">Steuerung der baulichen Umsetzung</p><h2 class="title">STET CLITA KASD GUBERGREN NO SEA TAKIMATA SANCTUS EST LOREM</h2><p class="body">Lorem ipsum dolor sit amet, consetetur sadipscing elitr, sed diam nonumy eirmod tempor invidunt ut labore et dolore magna aliquyam erat, sed diam voluptua.</p><span class="more">WEITERLESEN</span></article>
      <article class="card"><p class="cat">Marketing und Vertrieb</p><h2 class="title">STET CLITA KASD GUBERGREN NO SEA TAKIMATA SANCTUS EST LOREM</h2><p class="body">Lorem ipsum dolor sit amet, consetetur sadipscing elitr, sed diam nonumy eirmod tempor invidunt ut labore et dolore magna aliquyam erat, sed diam voluptua.</p><span class="more">WEITERLESEN</span></article>
    </div>
    <div class="footer">© 2017 Kessling Real Estate GmbH - Impressum</div>
  </div>
</section>

</body>
</html>
```